Fun Location App for users to earn rewards and vouchers everywhere they go

Jorvix is a social app where users can collect rewards when they travel + complete quests at different location to get rewards.

We would like a design of an app that has these features/function
1) Login/Signup Page
2) HomePage - A Map with your current location
- Show the location/stores aroudn
- Have a bag tab to press and get rewards
3) Quests Tab = show all the available tasks
4) Exchange Tab = all the items available for exchange vouchers and can click to know more
5) Wallet Tab = user profile + vouchers in their wallet
6) Partners Tab = Showcase all the partners and can click to know more
7) Claim functions

We have attached a visual example. Do feel free to change what is best fit too. We do need to exact measurements as well to create the app

Target Market(s)

Fun, people who like rewards and interact with friends

Font styles to use
Sans Serif

Colors
f78f20
fbed22
fbee3e

Requirements
Must have
• Yellow, fun interactive feeling.
Nice to have
• Pop up when click on things
Should not have
• nil

```html
<!DOCTYPE html>
<html lang="en">
<head>
<meta charset="utf-8">
<title>Jorvix – App Screens</title>
<link rel="stylesheet" href="https://fonts.googleapis.com/css2?family=Poppins:wght@400;500;600;700&display=swap">
<style>
:root{
  --orange:#f78f20;
  --yellow:#fbed22;
  --yellow-soft:#fbee3e;
  --ink:#2b2b2b;
  --muted:#6d6d6d;
  --page:#f5f8fc;
  --card:#ffffff;
  --map:#1f1f1f;
  --map-light:#2c2c2c;
  --social:#3d5ba9;
  --grad-bar:linear-gradient(90deg,var(--orange),var(--yellow));
  --grad-head:linear-gradient(60deg,var(--orange) 15%,var(--yellow) 100%);
}
*{box-sizing:border-box;margin:0;padding:0}
html,body{width:1200px;height:2562px;overflow:hidden}
body{font-family:"Poppins",sans-serif;background:var(--page);color:var(--ink);position:relative}
.hero{position:absolute;left:0;top:0;width:1200px;height:905px;overflow:hidden;
  background:linear-gradient(120deg,var(--yellow) 0%,var(--yellow-soft) 35%,#f9b52a 75%,var(--orange) 100%)}
.blob{position:absolute;border-radius:50%;background:rgba(255,255,255,.12)}
.screen-title{position:absolute;width:300px;text-align:center;font-size:17px;font-weight:600;color:#333;letter-spacing:.2px}
.screen{position:absolute;width:280px;background:var(--card);border-radius:26px;overflow:hidden;
  box-shadow:0 10px 30px rgba(120,130,160,.18)}
.abs{position:absolute}
.head{position:absolute;left:0;top:0;width:280px;height:147px;background:var(--grad-head);border-radius:26px;
  color:#fff;text-align:center}
.head .welcome{position:absolute;width:100%;top:38px;font-size:13px;font-weight:500}
.head .brand{position:absolute;width:100%;top:58px;font-size:40px;font-weight:700;letter-spacing:-.5px;line-height:1}
.form-title{position:absolute;width:100%;text-align:center;font-size:20px;font-weight:600;color:var(--orange);letter-spacing:1px}
.field{position:absolute;left:23px;width:235px;height:30px;border:1px solid #8d8d8d;border-radius:16px;
  font-size:11px;color:#555;padding-left:16px;line-height:28px}
.btn{position:absolute;left:23px;width:235px;height:34px;border-radius:3px;background:var(--grad-bar);
  color:#fff;font-weight:600;font-size:12px;text-align:center;line-height:34px;box-shadow:0 6px 12px rgba(247,143,32,.22)}
.btn-social{background:var(--social);box-shadow:none;font-size:10px}
.btn-plain{background:#fff;color:var(--ink);box-shadow:0 3px 10px rgba(0,0,0,.1);font-size:10px}
.small{position:absolute;font-size:9px;color:#555}
.footer-ask{position:absolute;width:100%;text-align:center;font-size:11px;color:#444}
.footer-ask b{color:var(--orange);font-weight:600}
.powered{position:absolute;width:100%;text-align:center;font-size:7px;color:#666;line-height:1.3}
.powered b{display:block;font-size:9px;color:#333;font-weight:600}
.map{position:absolute;left:0;top:0;width:280px;height:560px;
  background:radial-gradient(circle at 40% 45%,var(--map-light) 0%,var(--map) 75%)}
.gear{position:absolute;right:22px;top:16px;width:26px;height:26px}
.tally{position:absolute;left:22px;top:485px;width:236px;height:48px;border-radius:10px;background:rgba(40,40,40,.92);
  color:#fff;display:flex;align-items:center}
.tally .count{text-align:center;line-height:1}
.tally .count strong{display:block;font-size:20px;font-weight:600}
.tally .count span{font-size:9px}
.tally .bag{position:absolute;right:12px;top:8px;width:32px;height:32px;border-radius:4px;background:var(--orange);
  display:flex;align-items:center;justify-content:center}
.nav{position:absolute;left:0;bottom:0;width:280px;height:50px;background:#fff;border-radius:0 0 26px 26px;
  display:flex;justify-content:space-around;align-items:center;padding:0 14px}
.nav svg{width:24px;height:24px}
.quest-item{position:absolute;left:16px;width:248px;height:66px;display:flex;align-items:center}
.quest-item .thumb{width:74px;height:54px;border-radius:4px;flex:none}
.quest-item .info{margin-left:10px;flex:1}
.quest-item .info strong{display:block;font-size:12px;font-weight:600}
.quest-item .info span{font-size:9px;color:var(--muted)}
.pill{font-size:8px;color:#fff;background:var(--orange);border-radius:10px;padding:3px 9px;align-self:flex-start;margin-top:6px}
</style>
</head>
<body>

<svg width="0" height="0" style="position:absolute" aria-hidden="true">
  <defs>
    <symbol id="i-gear" viewBox="0 0 24 24"><g fill="#fff"><circle cx="12" cy="12" r="7"/><rect x="10" y="1" width="4" height="6" rx="1"/><rect x="10" y="17" width="4" height="6" rx="1"/><rect x="1" y="10" width="6" height="4" rx="1"/><rect x="17" y="10" width="6" height="4" rx="1"/><rect x="10" y="1" width="4" height="6" rx="1" transform="rotate(45 12 12)"/><rect x="10" y="1" width="4" height="6" rx="1" transform="rotate(-45 12 12)"/><rect x="10" y="17" width="4" height="6" rx="1" transform="rotate(45 12 12)"/><rect x="10" y="17" width="4" height="6" rx="1" transform="rotate(-45 12 12)"/></g><circle cx="12" cy="12" r="3" fill="#222"/></symbol>
    <symbol id="i-list" viewBox="0 0 24 24"><g fill="none" stroke="#555" stroke-width="1.8"><rect x="5" y="4" width="14" height="18" rx="2"/><path d="M9 3h6v3H9zM8 10h8M8 14h8M8 18h5"/></g></symbol>
    <symbol id="i-swap" viewBox="0 0 24 24"><g fill="#555"><path d="M3 8l5-5v3h9v4H8v3z"/><path d="M21 16l-5 5v-3H7v-4h9v-3z"/></g></symbol>
    <symbol id="i-navpin" viewBox="0 0 24 24"><path d="M12 1C7 1 4 5 4 9.5 4 15 12 23 12 23s8-8 8-13.5C20 5 17 1 12 1z" fill="#fbd428"/><circle cx="12" cy="9.5" r="3.5" fill="#fff"/></symbol>
    <symbol id="i-wallet" viewBox="0 0 24 24"><g fill="#555"><rect x="2" y="6" width="20" height="14" rx="2"/></g><rect x="14" y="10" width="8" height="6" rx="1" fill="#fff"/><circle cx="17" cy="13" r="1.3" fill="#555"/></symbol>
    <symbol id="i-heart" viewBox="0 0 24 24"><path d="M12 21S2 14.5 2 8.5A5 5 0 0 1 12 6a5 5 0 0 1 10 2.5C22 14.5 12 21 12 21z" fill="#555"/><path d="M7 11l3 3 3-3 3 3" fill="none" stroke="#fff" stroke-width="1.6"/></symbol>
    <symbol id="i-bag" viewBox="0 0 24 24"><path d="M5 8h14l-1 13H6z" fill="#fff"/><path d="M9 8V6a3 3 0 0 1 6 0v2" fill="none" stroke="#fff" stroke-width="1.8"/></symbol>
    <symbol id="i-back" viewBox="0 0 24 24"><path d="M15 5l-7 7 7 7" fill="none" stroke="#fff" stroke-width="2.4" stroke-linecap="round"/></symbol>
  </defs>
</svg>

<section class="hero">
  <div class="blob" style="left:-120px;top:-80px;width:520px;height:520px"></div>
  <div class="blob" style="left:820px;top:480px;width:560px;height:560px"></div>
  <div class="blob" style="left:300px;top:620px;width:300px;height:300px"></div>

  <div class="screen quest-screen" style="left:460px;top:60px;height:790px">
    <div class="head" style="height:118px;border-radius:26px">
      <div class="abs" style="left:24px;top:34px;font-size:24px;font-weight:700">Quest Time !</div>
      <div class="abs" style="left:24px;top:70px;font-size:12px;font-weight:500">Challenges to earn rewards !</div>
      <svg class="gear" style="top:16px"><use href="#i-gear"/></svg>
    </div>
    <div class="quest-item" style="top:136px"><div class="thumb" role="img" aria-label="Partner store promo image" style="background:linear-gradient(120deg,#7dbb2e,#3f9a3a)"></div><div class="info"><strong>Corner Deli</strong><span>$1 off for any item</span></div><div class="pill">Challenge</div></div>
    <div class="quest-item" style="top:214px"><div class="thumb" role="img" aria-label="Partner store promo image" style="background:linear-gradient(120deg,#f7a030,#e2542a)"></div><div class="info"><strong>Corner Deli</strong><span>$1 off for any item</span></div><div class="pill">Challenge</div></div>
    <div class="quest-item" style="top:292px"><div class="thumb" role="img" aria-label="Food dish photo" style="background:linear-gradient(120deg,#7a2f22,#c3563a)"></div><div class="info"><strong>Corner Deli</strong><span>$1 off for any item</span></div><div class="pill">Challenge</div></div>
    <div class="quest-item" style="top:370px"><div class="thumb" role="img" aria-label="Seasonal shop promo image" style="background:linear-gradient(120deg,#e8d2b0,#8b6a4a)"></div><div class="info"><strong>Corner Deli</strong><span>$1 off for any item</span></div><div class="pill">Challenge</div></div>
    <div class="quest-item" style="top:448px"><div class="thumb" role="img" aria-label="Partner store promo image" style="background:linear-gradient(120deg,#7dbb2e,#3f9a3a)"></div><div class="info"><strong>Corner Deli</strong><span>$1 off for any item</span></div><div class="pill">Challenge</div></div>
    <div class="quest-item" style="top:526px"><div class="thumb" role="img" aria-label="Partner store promo image" style="background:linear-gradient(120deg,#f7a030,#e2542a)"></div><div class="info"><strong>Corner Deli</strong><span>$1 off for any item</span></div><div class="pill">Challenge</div></div>
    <div class="quest-item" style="top:604px"><div class="thumb" role="img" aria-label="Food dish photo" style="background:linear-gradient(120deg,#7a2f22,#c3563a)"></div><div class="info"><strong>Corner Deli</strong><span>$1 off for any item</span></div><div class="pill">Challenge</div></div>
    <nav class="nav" style="box-shadow:0 -4px 12px rgba(0,0,0,.06)">
      <svg><use href="#i-list"/></svg><svg><use href="#i-swap"/></svg><svg><use href="#i-navpin"/></svg><svg><use href="#i-wallet"/></svg><svg><use href="#i-heart"/></svg>
    </nav>
  </div>
</section>

<h2 class="screen-title" style="left:79px;top:938px">Splash Screen</h2>
<h2 class="screen-title" style="left:453px;top:938px">OTP Login</h2>
<h2 class="screen-title" style="left:825px;top:938px">Login</h2>

<div class="screen splash" style="left:90px;top:985px;height:600px;background:linear-gradient(160deg,#fffdf3,#fff6d8 60%,#fffbe9)">
  <div class="abs" style="left:15px;top:103px;width:250px;height:250px;border-radius:50%;background:#fff"></div>
  <div class="abs" style="left:0;top:233px;width:280px;text-align:center;font-size:40px;font-weight:700;color:#3a3a3a;letter-spacing:-.5px;line-height:1">Jorvix</div>
</div>

<div class="screen otp" style="left:463px;top:977px;height:601px">
  <header class="head"><div class="welcome">Welcome to</div><div class="brand">Jorvix</div></header>
  <div class="form-title" style="top:170px">OTP LOG IN</div>
  <div class="field" style="top:229px">Mobile No</div>
  <div class="field" style="top:283px">Enter OTP</div>
  <div class="small" style="left:0;width:100%;text-align:center;top:324px">Did not receive OTP ?</div>
  <div class="btn" style="top:359px">Sign in</div>
  <div class="footer-ask" style="top:538px">Don't have an account? <b>Sign Up</b></div>
  <div class="powered" style="top:571px">Powered By<b>Lumen Works</b></div>
</div>

<div class="screen login" style="left:836px;top:985px;height:601px">
  <header class="head"><div class="welcome">Welcome to</div><div class="brand">Jorvix</div></header>
  <div class="form-title" style="top:170px">SIGN IN</div>
  <div class="field" style="top:229px">Email</div>
  <div class="field" style="top:283px">Password</div>
  <div class="small" style="right:23px;top:324px">Forgot password?</div>
  <div class="btn" style="top:359px">Sign in</div>
  <div class="btn btn-social" style="top:432px">Connect with Circlebook</div>
  <div class="btn btn-plain" style="top:484px">Connect with Searchly</div>
  <div class="footer-ask" style="top:538px">Don't have an account? <b>Sign Up</b></div>
  <div class="powered" style="top:571px">Powered By<b>Lumen Works</b></div>
</div>

<h2 class="screen-title" style="left:79px;top:1654px">Sign Up</h2>
<h2 class="screen-title" style="left:453px;top:1654px">Home Screen : Empty Bag</h2>
<h2 class="screen-title" style="left:825px;top:1654px">Home Screen : Bag with Items</h2>

<div class="screen signup" style="left:90px;top:1700px;height:752px">
  <header class="head" style="height:165px;border-radius:26px 26px 0 0">
    <svg class="abs" style="left:10px;top:48px;width:22px;height:22px"><use href="#i-back"/></svg>
    <div class="brand" style="top:72px;font-size:44px">Jorvix</div>
  </header>
  <div class="form-title" style="top:192px">SIGN UP</div>
  <div class="field" style="top:255px;left:10px;width:260px;height:34px;line-height:32px;font-size:13px">Full Name</div>
  <div class="field" style="top:315px;left:10px;width:260px;height:34px;line-height:32px;font-size:13px">Username</div>
  <div class="field" style="top:374px;left:10px;width:260px;height:34px;line-height:32px;font-size:13px">Email</div>
  <div class="field" style="top:433px;left:10px;width:260px;height:34px;line-height:32px;font-size:13px">Date of Birth</div>
  <div class="field" style="top:493px;left:10px;width:260px;height:34px;line-height:32px;font-size:13px">Referral Code</div>
  <div class="abs" style="left:28px;top:558px;font-size:13px;color:#444">Gender</div>
  <div class="abs" style="left:96px;top:552px;width:66px;height:28px;line-height:28px;text-align:center;font-size:13px;background:#fff;box-shadow:0 2px 8px rgba(0,0,0,.1);border-radius:3px">Female</div>
  <div class="abs" style="left:190px;top:552px;width:66px;height:28px;line-height:28px;text-align:center;font-size:13px;color:#fff;background:var(--orange);border-radius:3px">Male</div>
  <div class="btn" style="top:608px;left:10px;width:260px;height:36px;line-height:36px;font-size:14px">Sign Up</div>
  <div class="abs" style="left:10px;top:665px;width:262px;font-size:9.5px;color:#555;line-height:1.35">By Signing up you have agreed to Terms of Use and Privacy Policy on Jorvix PVT LTD</div>
  <div class="powered" style="top:716px">Powered By<b>Lumen Works</b></div>
</div>

<div class="screen home" style="left:463px;top:1692px;height:603px;background:var(--map)">
  <div class="map" role="img" aria-label="Dark street map of the city centre with nearby partner store locations"></div>
  <svg class="gear"><use href="#i-gear"/></svg>
  <div class="tally">
    <div class="count" style="width:70px"><strong>0</strong><span>Jorvcoins</span></div>
    <div class="count" style="width:70px"><strong>0</strong><span>Vouchers</span></div>
    <div class="bag"><svg width="20" height="20"><use href="#i-bag"/></svg></div>
  </div>
  <nav class="nav"><svg><use href="#i-list"/></svg><svg><use href="#i-swap"/></svg><svg><use href="#i-navpin"/></svg><svg><use href="#i-wallet"/></svg><svg><use href="#i-heart"/></svg></nav>
</div>

<div class="screen home" style="left:836px;top:1700px;height:603px;background:var(--map)">
  <div class="map" role="img" aria-label="Dark street map of the city centre with nearby partner store locations"></div>
  <svg class="gear"><use href="#i-gear"/></svg>
  <div class="tally">
    <div class="count" style="width:70px"><strong>5</strong><span>Jorvcoins</span></div>
    <div class="count" style="width:70px"><strong>5000</strong><span>Vouchers</span></div>
    <div class="bag"><svg width="20" height="20"><use href="#i-bag"/></svg></div>
  </div>
  <nav class="nav"><svg><use href="#i-list"/></svg><svg><use href="#i-swap"/></svg><svg><use href="#i-navpin"/></svg><svg><use href="#i-wallet"/></svg><svg><use href="#i-heart"/></svg></nav>
</div>

</body>
</html>
```